Velmor Glazing

Modern glazing company specializing in commercial fit outs, pool fencing, frameless showers and glass splash backs, im after a very young/modern logo, it doesnt have to be revelent to glazing and a classy "boss like" design for the card. thank you in advanced

im thinking carbon fiber back ground or something along that line with bright orange wording or something maybe, open to suggestions 

Fencing

company name, name, phone and products

```html
<!DOCTYPE html>
<html lang="en">
<head>
<meta charset="utf-8">
<title>Velmor Glazing – Business Card</title>
<link rel="stylesheet" href="https://fonts.googleapis.com/css2?family=Marcellus&family=Didact+Gothic&display=swap">
<style>
  :root {
    --stage-light: #a9a9a9;
    --stage-dark: #5e5e5e;
    --card-base: #161616;
    --card-edge: #0c0c0c;
    --accent-orange: #e2742a;
    --muted-grey: #b9b9b9;
    --label-grey: #d0d0d0;
  }
  html, body {
    margin: 0;
    padding: 0;
    overflow: hidden;
  }
  .stage {
    width: 1200px;
    height: 791px;
    position: relative;
    overflow: hidden;
    background: radial-gradient(ellipse at 45% 40%, var(--stage-light) 0%, #8a8a8a 45%, var(--stage-dark) 100%);
  }
  .card {
    position: absolute;
    top: 238px;
    width: 500px;
    height: 305px;
    box-sizing: border-box;
    background: linear-gradient(135deg, #1d1d1d 0%, var(--card-base) 55%, var(--card-edge) 100%);
    box-shadow: 0 14px 30px rgba(0, 0, 0, 0.45);
  }
  .card--front { left: 70px; }
  .card--back { left: 630px; }

  /* Front */
  .brand {
    position: absolute;
    left: 70px;
    top: 126px;
    display: flex;
    align-items: center;
    gap: 22px;
  }
  .brand__mark {
    width: 48px;
    height: 48px;
    background: var(--accent-orange);
  }
  .brand__name {
    font-family: "Marcellus", serif;
    font-size: 38px;
    color: var(--accent-orange);
    letter-spacing: 1px;
    margin: 0;
    font-weight: 400;
  }

  /* Back */
  .contact {
    position: absolute;
    left: 40px;
    top: 118px;
  }
  .contact__name {
    font-family: "Marcellus", serif;
    font-size: 36px;
    color: var(--accent-orange);
    margin: 0;
    font-weight: 400;
    letter-spacing: 1px;
  }
  .contact__role {
    font-family: "Didact Gothic", sans-serif;
    font-size: 20px;
    color: var(--muted-grey);
    margin: 0 0 0 82px;
    letter-spacing: 2px;
  }
  .contact__phone {
    font-family: "Didact Gothic", sans-serif;
    font-size: 22px;
    color: var(--accent-orange);
    margin: 36px 0 0 70px;
    letter-spacing: 2px;
  }
  .products {
    position: absolute;
    left: 320px;
    top: 48px;
  }
  .products__label {
    display: inline-block;
    font-family: "Didact Gothic", sans-serif;
    font-size: 11px;
    letter-spacing: 1px;
    color: #2a2a2a;
    background: var(--label-grey);
    border: 1px solid #ffffff;
    padding: 0 5px;
    margin: 0 0 8px 14px;
  }
  .products__list {
    list-style: none;
    margin: 0;
    padding: 0;
    font-family: "Didact Gothic", sans-serif;
    font-size: 13px;
    line-height: 18px;
    color: var(--accent-orange);
  }
  .products__list li:nth-child(2) { padding-left: 12px; }
  .products__list li:nth-child(3) { padding-left: 6px; }
  .products__list li:nth-child(4) { padding-left: 16px; }
</style>
</head>
<body>
  <main class="stage">
    <section class="card card--front" aria-label="Card front">
      <div class="brand">
        <span class="brand__mark"></span>
        <h1 class="brand__name">Velmor Glazing</h1>
      </div>
    </section>

    <section class="card card--back" aria-label="Card back">
      <div class="products">
        <span class="products__label">PRODUCTS</span>
        <ul class="products__list">
          <li>- commercial fit outs</li>
          <li>- pool fencing</li>
          <li>- frameless showers</li>
          <li>and glass splash backs.</li>
        </ul>
      </div>
      <div class="contact">
        <h2 class="contact__name">Dane Morrow</h2>
        <p class="contact__role">owner</p>
        <p class="contact__phone">0491 570 218</p>
      </div>
    </section>
  </main>
</body>
</html>
```